Typing Service Business Card Design

Need a new business card design for new logo update. The Keyline Crew is an outsourced typing service. We type audio / voice files into word documents. We are a professional service that is recognised in the industry over the past 15 years and have a strong connection to our brand. The final design should be professional, simple, yet effective.

Business

Contact Information for Business Card

Rosalind Varga
Director

rosalind@kbq.com.au
www.thekeylinecrewbase.com.au

```html
<!DOCTYPE html>
<html lang="en">
<head>
<meta charset="utf-8">
<title>The Keyline Crew — Business Card</title>
<link href="https://fonts.googleapis.com/css2?family=Jost:wght@400;500;600&display=swap" rel="stylesheet">
<style>
  :root {
    --backdrop: #b89468;
    --card-black: #0b0b0c;
    --card-sheen: #232325;
    --magenta: #d42f8e;
    --ink-white: #f4f4f4;
    --rule-grey: #3a3a3c;
  }
  * { margin: 0; padding: 0; box-sizing: border-box; }
  html, body {
    width: 1200px; height: 900px; overflow: hidden;
    background: var(--backdrop);
    font-family: "Jost", "Futura", sans-serif;
  }
  .stage { position: relative; width: 1200px; height: 900px; }
  .card {
    position: absolute;
    width: 520px; height: 318px;
    border-radius: 14px;
    background: linear-gradient(160deg, var(--card-sheen) 0%, var(--card-black) 45%, var(--card-black) 100%);
    box-shadow: 0 18px 40px rgba(0,0,0,0.45);
    color: var(--ink-white);
    overflow: hidden;
  }
  .card--front { left: 110px; top: 110px; }
  .card--back { left: 570px; top: 470px; }

  /* front */
  .brand {
    position: absolute; left: 0; right: 0; top: 92px;
    text-align: center;
  }
  .brand__name {
    display: inline-flex; align-items: center; gap: 12px;
    font-size: 34px; font-weight: 500; color: var(--magenta);
    letter-spacing: 0.5px;
  }
  .brand__dot {
    width: 14px; height: 14px; border-radius: 50%;
    background: var(--magenta);
  }
  .brand__tagline {
    display: block; margin-top: 6px;
    padding-left: 150px;
    font-size: 17px; font-weight: 400; color: var(--ink-white);
  }
  .front__rule {
    position: absolute; left: 0; right: 0; top: 200px;
    height: 1px; background: var(--rule-grey);
  }
  .front__web {
    position: absolute; left: 0; right: 0; bottom: 44px;
    text-align: center;
    font-size: 13px; letter-spacing: 2px; color: var(--ink-white);
  }

  /* back */
  .back__accent {
    position: absolute; left: 34px; top: 0; bottom: 0;
    width: 2px; background: var(--magenta);
  }
  .contact {
    position: absolute; left: 78px; top: 92px;
  }
  .contact__name {
    font-size: 22px; font-weight: 600; color: var(--magenta);
    letter-spacing: 0.3px;
  }
  .contact__role {
    font-size: 15px; margin-top: 2px; color: var(--ink-white);
  }
  .contact__list { list-style: none; margin-top: 18px; }
  .contact__item {
    display: flex; align-items: center; gap: 9px;
    font-size: 16px; line-height: 24px; color: var(--ink-white);
  }
  .contact__icon { width: 14px; height: 14px; flex: none; }
</style>
</head>
<body>
<main class="stage">
  <section class="card card--front" aria-label="Business card front">
    <div class="brand">
      <span class="brand__name"><span class="brand__dot"></span>The Keyline Crew</span>
      <span class="brand__tagline">You speak. We key.</span>
    </div>
    <div class="front__rule"></div>
    <p class="front__web">www.thekeylinecrewbase.com.au</p>
  </section>

  <section class="card card--back" aria-label="Business card back">
    <div class="back__accent"></div>
    <div class="contact">
      <h1 class="contact__name">Rosalind Varga</h1>
      <p class="contact__role">Director</p>
      <ul class="contact__list">
        <li class="contact__item">
          <svg class="contact__icon" viewBox="0 0 14 14" aria-hidden="true">
            <circle cx="7" cy="7" r="7" fill="var(--magenta)"/>
            <rect x="3.2" y="4.5" width="7.6" height="5" rx="0.6" fill="none" stroke="#0b0b0c" stroke-width="1"/>
            <path d="M3.4 4.8 L7 7.4 L10.6 4.8" fill="none" stroke="#0b0b0c" stroke-width="1"/>
          </svg>
          rosalind@kbq.com.au
        </li>
        <li class="contact__item">
          <svg class="contact__icon" viewBox="0 0 14 14" aria-hidden="true">
            <circle cx="7" cy="7" r="7" fill="var(--magenta)"/>
            <circle cx="7" cy="7" r="3.8" fill="none" stroke="#0b0b0c" stroke-width="1"/>
            <ellipse cx="7" cy="7" rx="1.6" ry="3.8" fill="none" stroke="#0b0b0c" stroke-width="0.9"/>
            <line x1="3.2" y1="7" x2="10.8" y2="7" stroke="#0b0b0c" stroke-width="0.9"/>
          </svg>
          www.thekeylinecrewbase.com.au
        </li>
      </ul>
    </div>
  </section>
</main>
</body>
</html>
```